Business Card Design for a Design/Build Firm

Kestrel Forge Partners, Inc. is a firm providing construction professional project management and architectural design services to an international clientele. Contemporary. "Green" movement aware. Business card to have back design/logo. Cards will be on high gloss paper

Target Market(s)

Building Developers and Owners

Industry/Entity Type

Construction

Requirements
Nice to have
• We really would like to use the acronym "KFP" as main focal point fo card design. Company will be known as KFP.
Should not have
• No globes or abstract images of buildings.

```html
<!DOCTYPE html>
<html lang="en">
<head>
<meta charset="utf-8">
<title>KFP Business Card</title>
<link rel="stylesheet" href="https://fonts.googleapis.com/css2?family=PT+Sans:wght@400;700&display=swap">
<style>
  :root {
    --green-light: #9ccc3c;
    --green-mid: #5aa814;
    --green-dark: #1f7a0c;
    --green-deep: #17690a;
    --white: #ffffff;
    --page-top: #b4b4b4;
    --page-bottom: #e6e6e6;
    --shadow: rgba(0,0,0,0.28);
  }
  html, body {
    margin: 0;
    padding: 0;
    width: 1200px;
    height: 1000px;
    overflow: hidden;
  }
  body {
    background: linear-gradient(to bottom, var(--page-top), var(--page-bottom));
    font-family: "PT Sans", Arial, sans-serif;
    position: relative;
  }
  .card {
    position: absolute;
    top: 330px;
    width: 540px;
    height: 340px;
    box-shadow: 0 6px 16px var(--shadow);
    overflow: hidden;
    background: var(--white);
  }
  .card > svg { position: absolute; inset: 0; display: block; }
  .card--front { left: 40px; }
  .card--back { left: 620px; }

  .front-mark {
    position: absolute;
    left: 150px;
    top: 70px;
    display: flex;
    align-items: center;
    gap: 16px;
    color: var(--white);
    font-weight: 700;
    font-size: 110px;
    line-height: 1;
    letter-spacing: -2px;
  }
  .front-mark__dot {
    width: 34px; height: 34px;
    border-radius: 50%;
    background: var(--white);
  }

  .back-mark {
    position: absolute;
    left: 40px;
    top: 38px;
    color: var(--white);
    font-weight: 700;
    font-size: 50px;
    line-height: 1;
    letter-spacing: -1px;
  }
  .identity {
    position: absolute;
    right: 26px;
    top: 40px;
    text-align: right;
    color: var(--white);
    font-weight: 700;
  }
  .identity__name { font-size: 28px; line-height: 1.1; margin: 0; letter-spacing: 0.5px; }
  .identity__role { font-size: 22px; line-height: 1.2; margin: 2px 0 0; }

  .contact {
    position: absolute;
    right: 26px;
    top: 118px;
    margin: 0;
    padding: 0;
    list-style: none;
    color: var(--white);
    font-size: 11px;
    text-align: right;
  }
  .contact li {
    display: flex;
    justify-content: flex-end;
    align-items: center;
    gap: 8px;
    height: 16px;
  }
  .contact li.gap { margin-top: 12px; }
  .contact svg { width: 10px; height: 10px; flex: none; }
</style>
</head>
<body>

<section class="card card--front" aria-label="Card front">
  <svg viewBox="0 0 540 340" preserveAspectRatio="none">
    <defs>
      <radialGradient id="frontGreen" cx="0.6" cy="0.7" r="0.8">
        <stop offset="0" stop-color="var(--green-light)"/>
        <stop offset="0.6" stop-color="var(--green-mid)"/>
        <stop offset="1" stop-color="var(--green-dark)"/>
      </radialGradient>
    </defs>
    <rect width="540" height="340" fill="url(#frontGreen)"/>
    <path d="M0,222 C80,255 170,250 240,226" fill="none" stroke="var(--green-deep)" stroke-width="8" opacity="0.45"/>
    <path d="M360,340 C372,280 395,230 430,226 C475,221 515,252 540,270" fill="none" stroke="var(--green-deep)" stroke-width="10" opacity="0.45"/>
    <path d="M0,232 C80,265 170,260 240,236 C270,226 285,252 300,300 L314,340 L0,340 Z" fill="var(--white)"/>
    <path d="M372,340 C384,290 404,250 432,244 C472,238 512,268 540,288 L540,340 Z" fill="var(--white)"/>
    <path d="M0,232 C80,265 170,260 240,236 C270,226 285,252 300,300 L314,340" fill="none" stroke="var(--white)" stroke-width="3"/>
    <path d="M364,340 C376,286 398,242 432,236 C474,230 514,260 540,280" fill="none" stroke="var(--white)" stroke-width="2.5"/>
  </svg>
  <div class="front-mark"><span class="front-mark__dot"></span><span>KFP</span></div>
</section>

<section class="card card--back" aria-label="Card back">
  <svg viewBox="0 0 540 340" preserveAspectRatio="none">
    <defs>
      <radialGradient id="backGreen" cx="0.45" cy="0.4" r="0.75">
        <stop offset="0" stop-color="var(--green-light)"/>
        <stop offset="0.6" stop-color="var(--green-mid)"/>
        <stop offset="1" stop-color="var(--green-dark)"/>
      </radialGradient>
    </defs>
    <rect width="540" height="340" fill="url(#backGreen)"/>
    <path d="M0,135 C60,128 110,140 110,185 C110,220 100,280 140,290 C250,305 340,262 430,270 C475,274 510,284 540,292 L540,340 L0,340 Z"
          fill="var(--green-deep)"/>
    <path d="M0,150 C50,140 80,160 75,200 C70,250 80,300 130,310 C250,325 340,278 440,288 C490,293 520,300 540,306 L540,340 L0,340 Z"
          fill="var(--white)"/>
    <path d="M0,135 C60,128 110,140 110,185 C110,220 100,280 140,290 C250,305 340,262 430,270 C475,274 510,284 540,292"
          fill="none" stroke="var(--white)" stroke-width="2.5"/>
  </svg>

  <div class="back-mark">KFP</div>

  <div class="identity">
    <p class="identity__name">NAME SURNAME</p>
    <p class="identity__role">Position</p>
  </div>

  <ul class="contact">
    <li>name@kfpartners.com
      <svg viewBox="0 0 10 10"><rect x="0.5" y="1.5" width="9" height="7" fill="none" stroke="#fff"/><path d="M0.5,1.5 L5,5.5 L9.5,1.5" fill="none" stroke="#fff"/></svg>
    </li>
    <li>+123 4567890
      <svg viewBox="0 0 10 10"><rect x="2.5" y="0.5" width="5" height="9" rx="1" fill="none" stroke="#fff"/><rect x="3.5" y="2" width="3" height="4" fill="#fff"/></svg>
    </li>
    <li class="gap">Lorem ipsum dolor sit amet felis nisl mauris ac ac lacus viva lorem
      <svg viewBox="0 0 10 10"><path d="M0.5,5 L5,0.8 L9.5,5 M2,4 V9.5 H8 V4" fill="none" stroke="#fff" stroke-width="1.4"/></svg>
    </li>
    <li class="gap">www.kfpartners.com
      <svg viewBox="0 0 10 10"><rect x="0.5" y="0.5" width="9" height="6.5" fill="none" stroke="#fff"/><path d="M3,9.5 H7 M5,7 V9.5" stroke="#fff"/></svg>
    </li>
    <li>chirpnet.com/kfpartners
      <svg viewBox="0 0 10 10"><circle cx="5" cy="5" r="4" fill="#fff"/></svg>
    </li>
    <li>facelink.com/kfpartners
      <svg viewBox="0 0 10 10"><circle cx="5" cy="5" r="4" fill="#fff"/></svg>
    </li>
  </ul>
</section>

</body>
</html>
```